International Perfume distribution Company needs a stationary design

We are a perfume development and distribution company named VELTRO and based in Sao Paulo Brazil. Basically we licence brazilian and international brands and celebrities to develop and distribute its fragrances and perfumes in Brazil. Our current licenced brands are: Darvel Quorra, Tessaro, Brixley Solvane fragrances and Lara Montebrino (brazilian soap opera celebrity).

We already have our logo and brand that reflects our massive distribution power in Brazil ("spraying our products accross Brazil") and we are also a branch of a big distribution company named MORANEX. It would be nice to mention it in our stationary ("uma divisao do grupo Moranex").

Industry/Entity Type

It Company

Requirements
Must have
• mention that Veltro is a division/branch of moranex using the following phrase: "uma divisão do grupo Moranex"

Use the logo signature: international fragrances

```html
<!DOCTYPE html>
<html lang="pt">
<head>
<meta charset="utf-8">
<title>Veltro – Business Card</title>
<link rel="stylesheet" href="https://fonts.googleapis.com/css2?family=Arimo:wght@400;700&display=swap">
<style>
  :root {
    --bg: #e4e4ea;
    --paper: #ffffff;
    --orange: #f0a41f;
    --purple: #3a2f8c;
    --ink: #1c1c1c;
    --rule: #c9c9cf;
    --white: #ffffff;
  }
  * { box-sizing: border-box; margin: 0; padding: 0; }
  html, body { width: 1200px; height: 987px; overflow: hidden; }
  body {
    background: var(--bg);
    font-family: "Arimo", Arial, sans-serif;
    position: relative;
  }
  .card {
    position: absolute;
    width: 540px;
    height: 310px;
    border-radius: 18px;
    overflow: hidden;
    top: 338px;
    box-shadow: 0 6px 18px rgba(0,0,0,0.12);
  }
  .card--front { left: 40px; background: var(--paper); }
  .card--back { left: 620px; background: var(--orange); }

  .front-bands { position: absolute; inset: 0; }

  .brand { position: absolute; left: 148px; top: 34px; }
  .brand__row { display: flex; align-items: center; gap: 14px; }
  .brand__dot { width: 42px; height: 42px; border-radius: 50%; background: var(--orange); }
  .brand__name {
    font-weight: 400; font-size: 60px; line-height: 1;
    color: var(--purple); letter-spacing: 2px;
  }
  .brand__tagline {
    margin: 4px 0 0 58px;
    font-size: 16px; color: var(--purple); letter-spacing: 0.5px;
  }

  .address {
    position: absolute; left: 40px; top: 150px; width: 200px;
    text-align: right; font-size: 17px; line-height: 1.35; color: var(--ink);
  }
  .divider {
    position: absolute; left: 256px; top: 146px;
    width: 1px; height: 76px; background: var(--rule);
  }
  .contacts {
    position: absolute; left: 272px; top: 146px;
    list-style: none; font-size: 17px; line-height: 1.45; color: var(--ink);
  }
  .contacts li { display: flex; align-items: center; gap: 8px; }
  .contacts svg { width: 14px; height: 14px; fill: var(--purple); flex: none; }

  .holder {
    position: absolute; right: 30px; bottom: 16px;
    color: var(--white); font-size: 18px;
  }
  .holder__name { font-weight: 700; font-size: 25px; }

  .back-brand {
    position: absolute; left: 0; right: 0; top: 70px;
    display: flex; justify-content: center; align-items: center; gap: 16px;
  }
  .back-brand__dot { width: 56px; height: 56px; border-radius: 50%; background: var(--white); }
  .back-brand__name { font-size: 56px; font-weight: 400; color: var(--white); letter-spacing: 3px; }
  .back-lines {
    position: absolute; left: 0; right: 0; top: 178px;
    text-align: center; color: var(--white);
  }
  .back-lines__division { font-size: 22px; letter-spacing: 1.5px; }
  .back-lines__web { margin-top: 8px; font-size: 17px; letter-spacing: 3px; }
</style>
</head>
<body>

<section class="card card--front" aria-label="Front of business card">
  <svg class="front-bands" viewBox="0 0 540 310" aria-hidden="true">
    <polygon points="0,220 138,220 156,234 0,234" fill="var(--orange)"/>
    <polygon points="0,240 150,240 170,252 540,252 540,310 0,310" fill="var(--purple)"/>
  </svg>

  <div class="brand">
    <div class="brand__row">
      <span class="brand__dot"></span>
      <span class="brand__name">VELTRO</span>
    </div>
    <p class="brand__tagline">international fragrances</p>
  </div>

  <p class="address">00, Complex name<br>City, State 0042</p>
  <span class="divider"></span>
  <ul class="contacts">
    <li>
      <svg viewBox="0 0 16 16"><path d="M3 1h3l1.5 4-2 1.3a9 9 0 0 0 4.2 4.2L11 8.5l4 1.5v3a2 2 0 0 1-2 2A13 13 0 0 1 1 3a2 2 0 0 1 2-2z"/></svg>
      0987 654321
    </li>
    <li>
      <svg viewBox="0 0 16 16"><rect x="4" y="0.5" width="8" height="15" rx="1.5"/><rect x="5.5" y="2.5" width="5" height="9" fill="#fff"/></svg>
      0987 654321
    </li>
    <li>
      <svg viewBox="0 0 16 16"><rect x="0.5" y="3" width="15" height="10" rx="1"/><path d="M1 4l7 5 7-5" stroke="#fff" stroke-width="1.4" fill="none"/></svg>
      info@veltro.com
    </li>
  </ul>

  <p class="holder"><span class="holder__name">Your Name,</span> Title</p>
</section>

<section class="card card--back" aria-label="Back of business card">
  <div class="back-brand">
    <span class="back-brand__dot"></span>
    <span class="back-brand__name">VELTRO</span>
  </div>
  <div class="back-lines">
    <p class="back-lines__division">uma divisão do grupo moranex</p>
    <p class="back-lines__web">www.veltro.com</p>
  </div>
</section>

</body>
</html>
```